Marlowe Tindra Pale Ale Beer Label/Badge

We need a Beer Label designed for our first official beer to be launched under The marlowe Brand!!
It will be a Pale Ale Called "Tindra Pale Ale"!

The Marlowe has the largest Craft Beer & Cider selection in the Geelong & Surf Coast region. With a funky location and a relaxed vibe, Marlowe prides itself on serving delicious, unique seasonal food paired with Australia's best Craft Beer. The marlowe is the perfect setting for a relaxed afternoon or evening with friends and can package an experience for larger groups or corporate bookings.

The Marlowe Tavern brand has been growing for over a year and a half and the first label needs to integrate The marlowe Logo but at the same time bring a fresh, new and eye catching feel to it along with embracing the "Odysseus" story in which we will be naming future beers.

The story of Tindra is found via the following link
http://en.lorevault.example/wiki/Tindra_(legend)

We expect designers to research The marlowe Tavern brand along with the all important Craft Beer Market and demographics. This will, potentially, be the start of many more labels to come for the winning designer!!

Requirements
Must have
• The original "O" needs to be integrated into the new logo and as much as the Greek mythology is being used it needs to be certain that this is an original Australian Craft Beer in the modern age!!
strong, modern & unique!!
Nice to have
• Logo could have a depiction of Tindra
Should not have
• tackiness or cheap!!

```html
<!DOCTYPE html>
<html lang="en">
<head>
<meta charset="utf-8">
<title>Marlowe Tindra Pale Ale – Label</title>
<link rel="stylesheet" href="https://fonts.googleapis.com/css2?family=Oswald:wght@500;600&family=Montserrat:wght@500;700&family=Libre+Baskerville:ital,wght@1,700&family=Federo&display=swap">
<style>
  :root {
    --backdrop: #e8e5df;
    --label-cream: #efede2;
    --label-shade: #e2e0d3;
    --label-rim: #b4b2a6;
    --ale-red: #8d1e21;
    --ribbon-dark: #5f1315;
    --ink-brown: #3a2a22;
    --portrait-gold: #d9a13a;
    --portrait-dark: #3b1a12;
    --hop-red: #9a2a2c;
  }
  * { margin: 0; padding: 0; box-sizing: border-box; }
  html, body {
    width: 1200px; height: 900px; overflow: hidden;
    background: radial-gradient(ellipse at 50% 45%, #f2f0eb 0%, var(--backdrop) 70%, #d9d5cd 100%);
  }
  .label {
    position: absolute; left: 370px; top: 50px;
    width: 460px; height: 800px;
  }
  .label-shape { position: absolute; inset: 0; }
  .portrait {
    position: absolute; left: 152px; top: 85px;
    width: 156px; height: 156px; border-radius: 50%;
    background: radial-gradient(circle at 55% 45%, var(--portrait-gold) 0 52%, var(--portrait-dark) 53%);
  }
  .ribbon { position: absolute; left: 0; top: 270px; width: 460px; height: 130px; }
  .ribbon-name {
    position: absolute; left: 0; width: 460px; top: 278px;
    text-align: center; font-family: "Federo", sans-serif;
    font-size: 50px; color: var(--label-cream); letter-spacing: 1px;
  }
  .hops {
    position: absolute; left: 205px; top: 352px; width: 50px; height: 34px;
    border-radius: 40% 40% 50% 50%; background: var(--hop-red);
  }
  .style-name {
    position: absolute; left: 0; width: 460px; top: 392px;
    text-align: center; font-family: "Oswald", sans-serif; font-weight: 600;
    font-size: 106px; line-height: 1.1; color: var(--ale-red); letter-spacing: 1px;
  }
  .rule {
    position: absolute; left: 120px; width: 220px; top: 530px;
    border-top: 2px solid var(--ale-red);
  }
  .tagline {
    position: absolute; left: 0; width: 460px; top: 545px;
    text-align: center; font-family: "Montserrat", sans-serif; font-weight: 500;
    font-size: 23px; letter-spacing: 3px; color: var(--ink-brown);
  }
  .origin {
    position: absolute; top: 628px;
    font-family: "Libre Baskerville", serif; font-style: italic; font-weight: 700;
    font-size: 14px; color: var(--ale-red);
  }
  .origin-town { left: 36px; }
  .origin-state { right: 36px; }
  .brand-mark {
    position: absolute; left: 0; width: 460px; top: 616px;
    text-align: center; font-family: "Oswald", sans-serif; font-weight: 600;
    font-size: 30px; color: var(--ale-red);
  }
  .abv {
    position: absolute; left: 76px; top: 680px;
    font-family: "Montserrat", sans-serif; font-weight: 500;
    font-size: 30px; color: var(--ink-brown);
  }
  .brewery {
    position: absolute; left: 0; width: 460px; top: 694px;
    text-align: center; font-family: "Montserrat", sans-serif; color: var(--ink-brown);
  }
  .brewery-name { font-weight: 700; font-size: 20px; letter-spacing: 1px; line-height: 1; }
  .brewery-sub { font-weight: 500; font-size: 9px; letter-spacing: 2px; margin-top: 3px; }
</style>
</head>
<body>
  <div class="label">
    <svg class="label-shape" viewBox="0 0 460 800" width="460" height="800" aria-hidden="true">
      <defs>
        <linearGradient id="cream" x1="0" y1="0" x2="1" y2="0">
          <stop offset="0" stop-color="#dddbcd"/>
          <stop offset="0.35" stop-color="#efede2"/>
          <stop offset="0.7" stop-color="#efede2"/>
          <stop offset="1" stop-color="#d8d6c9"/>
        </linearGradient>
      </defs>
      <polygon points="0,68 230,0 460,68 460,732 230,800 0,732" fill="#f4f3ec" stroke="var(--label-rim)" stroke-width="2"/>
      <polygon points="12,76 230,13 448,76 448,724 230,787 12,724" fill="url(#cream)" stroke="var(--label-rim)" stroke-width="1.5"/>
    </svg>

    <div class="portrait" role="img" aria-label="Circular portrait illustration of Tindra in gold and dark brown"></div>

    <svg class="ribbon" viewBox="0 0 460 130" width="460" height="130" aria-hidden="true">
      <polygon points="0,38 70,30 70,92 0,100 22,68" fill="var(--ribbon-dark)"/>
      <polygon points="460,38 390,30 390,92 460,100 438,68" fill="var(--ribbon-dark)"/>
      <path d="M40,18 Q230,-8 420,18 L420,80 Q230,54 40,80 Z" fill="var(--ale-red)"/>
    </svg>
    <div class="ribbon-name">Tindra</div>
    <div class="hops" role="img" aria-label="Small cluster of hops"></div>

    <div class="style-name">PALE ALE</div>
    <div class="rule"></div>
    <div class="tagline">HANDCRAFTED BEER</div>

    <div class="origin origin-town">Kestrel Ridge</div>
    <div class="brand-mark">Marlowe</div>
    <div class="origin origin-state">Victoria, Australia</div>

    <div class="abv">5%</div>
    <div class="brewery">
      <div class="brewery-name">MARLOWE</div>
      <div class="brewery-sub">TAVERN + BREWERY</div>
    </div>
  </div>
</body>
</html>
```